The Quietly Broken Map of HOME and ways to endure every season

Not sure.It is about Life injustice and how to face the truth and deal with anything that comes.It touched on Love Identity Finance Emotions

Target Market(s)

18-55

Industry/Entity Type

Life Coaching

Requirements
Must have
• A line through 'Broken'
Nice to have
• An image that captures the interest

```html
<!DOCTYPE html>
<html lang="en">
<head>
<meta charset="utf-8">
<title>The Quietly Broken Map — Book Cover</title>
<link href="https://fonts.googleapis.com/css2?family=Herr+Von+Muellerhoff&family=Roboto:wght@300;700;900&family=Roboto+Condensed:wght@700&display=swap" rel="stylesheet">
<style>
  :root {
    --page: #ffffff;
    --sky-blue: #a9dbe7;
    --sky-light: #e6f4f8;
    --sky-white: #fafcfc;
    --mountain-teal: #6fb3c6;
    --mountain-rock: #5a4231;
    --mountain-grass: #b6b95a;
    --title-red: #ad0a0a;
    --ink: #0d0d0d;
    --author-white: #ffffff;
  }
  * { margin: 0; padding: 0; box-sizing: border-box; }
  html, body {
    width: 1200px;
    height: 1200px;
    overflow: hidden;
    background: var(--page);
  }
  .book-cover {
    position: absolute;
    left: 230px;
    top: 52px;
    width: 740px;
    height: 1095px;
    overflow: hidden;
    background: linear-gradient(120deg, var(--sky-blue) 0%, var(--sky-light) 38%, var(--sky-white) 70%, var(--page) 100%);
  }
  .cover-photo {
    position: absolute;
    left: 0;
    bottom: 0;
    width: 100%;
    height: 365px;
    background:
      radial-gradient(ellipse 45% 70% at 30% 100%, var(--mountain-rock) 0%, rgba(90,66,49,0.85) 55%, rgba(90,66,49,0) 100%),
      linear-gradient(180deg, rgba(250,252,252,0) 0%, var(--mountain-teal) 30%, #4f8ea0 60%, var(--mountain-grass) 100%);
  }
  .title-script {
    position: absolute;
    top: 95px;
    left: 0;
    width: 100%;
    text-align: center;
    font-family: "Herr Von Muellerhoff", cursive;
    font-size: 150px;
    line-height: 1;
    color: var(--ink);
    padding-left: 30px;
  }
  .title-struck {
    position: absolute;
    top: 222px;
    left: 0;
    width: 100%;
    text-align: center;
    font-family: "Roboto Condensed", sans-serif;
    font-weight: 700;
    font-size: 190px;
    line-height: 1;
    color: var(--title-red);
    padding-left: 30px;
  }
  .strike-line {
    position: absolute;
    top: 313px;
    left: 98px;
    width: 530px;
    height: 2px;
    background: var(--ink);
  }
  .title-main {
    position: absolute;
    top: 400px;
    left: 0;
    width: 100%;
    text-align: center;
    font-family: "Roboto", sans-serif;
    font-weight: 900;
    font-size: 160px;
    line-height: 1;
    color: var(--ink);
    padding-left: 30px;
  }
  .subtitle {
    position: absolute;
    top: 555px;
    left: 0;
    width: 100%;
    text-align: center;
    font-family: "Roboto", sans-serif;
    font-weight: 300;
    font-size: 50px;
    line-height: 1.1;
    color: var(--ink);
    padding-left: 30px;
  }
  .author {
    position: absolute;
    top: 990px;
    left: 0;
    width: 100%;
    text-align: center;
    font-family: "Roboto", sans-serif;
    font-weight: 700;
    font-size: 44px;
    color: var(--author-white);
    padding-left: 30px;
  }
</style>
</head>
<body>
  <main class="book-cover">
    <div class="cover-photo" role="img" aria-label="Photograph of a hiker standing on a rocky summit above misty blue mountain ranges and a green valley"></div>
    <p class="title-script">The Quietly</p>
    <h1 class="title-struck">BROKEN</h1>
    <div class="strike-line"></div>
    <p class="title-main">MAP</p>
    <p class="subtitle">of HOME and ways to<br>endure every season</p>
    <p class="author">DANA R VELLOWAY</p>
  </main>
</body>
</html>
```